Visitenkarte für Ergotherapiepraxis
Zielgruppe
Wir arbeiten mit Kindern und Erwachsene jeden Alters.
Diese Personen kommen mit Beeinträchtigungen (körperlich, seelisch, schulisch) im täglichen Leben zu uns. Wir unterstützen unsere Patienten die Beeinträchtigungen zu verringern oder zu kompensieren und so den Alltag besser bewältigen zu können.
Aufgabenstellung
Ein Design was Kinder und Erwachsene anspricht, aber nicht zu verspielt wirkt. Es soll vertrauenserweckend sein. Eventuell sollte die Visitenkarte ein "aufgehendes oder erblühendes oder aufsteigendes" Element enthalten (=zu Beginn war die Beeinträchtigung dann steigt die Lebensqualität als Folge der Behandlung)
Daten vorn:
Ergotherapiepraxis

```html
<!DOCTYPE html>
<html lang="de">
<head>
<meta charset="utf-8">
<title>Visitenkarte Ergotherapiepraxis – Farbvarianten</title>
<link href="https://fonts.googleapis.com/css2?family=Barlow:wght@300;400;500;600&display=swap" rel="stylesheet">
<style>
  :root {
    --page-bg: #ffffff;
    --card-bg: #f7f7f7;
    --ink-grey: #6b6b6b;
    --ghost: #e6e6e6;
    --white: #ffffff;
    --blue: #009fe0;
    --blue-accent: #3cc43c;
    --green: #0a9a3c;
    --green-accent: #f4c300;
    --red: #9b0000;
    --red-accent: #13994a;
  }
  html, body {
    margin: 0;
    padding: 0;
    width: 1200px;
    height: 2185px;
    overflow: hidden;
    background: var(--page-bg);
    font-family: "Barlow", Arial, sans-serif;
  }
  .sheet {
    width: 1200px;
    height: 2185px;
    display: flex;
    flex-direction: column;
  }
  .variant {
    flex: 1;
    display: flex;
    align-items: center;
    justify-content: center;
    gap: 60px;
  }
  .variant--blue  { --band: var(--blue);  --accent: var(--blue-accent); }
  .variant--green { --band: var(--green); --accent: var(--green-accent); }
  .variant--red   { --band: var(--red);   --accent: var(--red-accent); }

  .card {
    position: relative;
    width: 500px;
    height: 323px;
    background: var(--card-bg);
    box-shadow: 0 2px 10px rgba(0,0,0,0.12);
    overflow: hidden;
  }
  .band {
    position: absolute;
    left: 0;
    right: 0;
    background: var(--band);
  }

  /* Front */
  .card--front .band { top: 188px; height: 100px; }
  .mark {
    position: absolute;
    left: 240px;
    top: 42px;
    display: flex;
    align-items: center;
    gap: 10px;
  }
  .mark__dot {
    width: 22px;
    height: 22px;
    border-radius: 50%;
    background: var(--band);
  }
  .mark__name {
    font-size: 36px;
    font-weight: 500;
    color: var(--band);
    letter-spacing: 0.5px;
  }
  .tagline {
    position: absolute;
    left: 275px;
    top: 100px;
    font-size: 12px;
    font-weight: 500;
    color: var(--accent);
  }
  .practice {
    position: absolute;
    right: 24px;
    top: 150px;
    font-size: 28px;
    line-height: 1;
    white-space: nowrap;
  }
  .practice__main { color: var(--ink-grey); font-weight: 600; }
  .practice__rule { color: var(--accent); font-weight: 300; margin: 0 1px; }
  .practice__sub { color: var(--accent); font-weight: 300; }
  .contact {
    position: absolute;
    right: 24px;
    top: 200px;
    text-align: right;
    color: var(--white);
  }
  .contact__name { font-size: 22px; font-weight: 400; line-height: 1.3; }
  .contact__phone { font-size: 18px; font-weight: 400; line-height: 1.3; }
  .address {
    position: absolute;
    left: 22px;
    top: 292px;
    font-size: 16px;
    font-weight: 600;
    color: var(--accent);
    white-space: nowrap;
  }

  /* Back */
  .card--back .band { top: 222px; height: 64px; }
  .ghost-mark {
    position: absolute;
    left: 180px;
    top: 60px;
    display: flex;
    align-items: center;
    gap: 14px;
  }
  .ghost-mark__dot {
    width: 30px;
    height: 30px;
    border-radius: 50%;
    background: var(--ghost);
  }
  .ghost-mark__name {
    font-size: 56px;
    font-weight: 500;
    color: var(--ghost);
  }
  .therapist-label {
    position: absolute;
    right: 24px;
    top: 194px;
    font-size: 19px;
    line-height: 1;
    white-space: nowrap;
  }
  .therapist-label__main { color: var(--accent); font-weight: 600; }
  .therapist-label__rule { color: var(--band); font-weight: 300; margin: 0 1px; }
  .therapist-label__sub { color: var(--accent); font-weight: 300; }
</style>
</head>
<body>
<main class="sheet">

  <section class="variant variant--blue">
    <article class="card card--back">
      <div class="ghost-mark"><span class="ghost-mark__dot"></span><span class="ghost-mark__name">Aufwind</span></div>
      <div class="therapist-label"><span class="therapist-label__main">Behandelnder</span><span class="therapist-label__rule">|</span><span class="therapist-label__sub">Therapeut/in:</span></div>
      <div class="band"></div>
    </article>
    <article class="card card--front">
      <div class="mark"><span class="mark__dot"></span><span class="mark__name">Aufwind</span></div>
      <div class="tagline">…für Ihre Lebensqualität</div>
      <div class="band"></div>
      <div class="practice"><span class="practice__main">Ergotherapie</span><span class="practice__rule">|</span><span class="practice__sub">praxis</span></div>
      <div class="contact">
        <div class="contact__name">Marlene Kessler</div>
        <div class="contact__phone">Tel. 034512/48127</div>
      </div>
      <div class="address">Am Weidenhof 12 | 15837 Baruth, OT Lenkau</div>
    </article>
  </section>

  <section class="variant variant--green">
    <article class="card card--back">
      <div class="ghost-mark"><span class="ghost-mark__dot"></span><span class="ghost-mark__name">Aufwind</span></div>
      <div class="therapist-label"><span class="therapist-label__main">Behandelnder</span><span class="therapist-label__rule">|</span><span class="therapist-label__sub">Therapeut/in:</span></div>
      <div class="band"></div>
    </article>
    <article class="card card--front">
      <div class="mark"><span class="mark__dot"></span><span class="mark__name">Aufwind</span></div>
      <div class="tagline">…für Ihre Lebensqualität</div>
      <div class="band"></div>
      <div class="practice"><span class="practice__main">Ergotherapie</span><span class="practice__rule">|</span><span class="practice__sub">praxis</span></div>
      <div class="contact">
        <div class="contact__name">Marlene Kessler</div>
        <div class="contact__phone">Tel. 034512/48127</div>
      </div>
      <div class="address">Am Weidenhof 12 | 15837 Baruth, OT Lenkau</div>
    </article>
  </section>

  <section class="variant variant--red">
    <article class="card card--front">
      <div class="mark"><span class="mark__dot"></span><span class="mark__name">Aufwind</span></div>
      <div class="tagline">…für Ihre Lebensqualität</div>
      <div class="band"></div>
      <div class="practice"><span class="practice__main">Ergotherapie</span><span class="practice__rule">|</span><span class="practice__sub">praxis</span></div>
      <div class="contact">
        <div class="contact__name">Marlene Kessler</div>
        <div class="contact__phone">Tel. 034512/48127</div>
      </div>
      <div class="address">Am Weidenhof 12 | 15837 Baruth, OT Lenkau</div>
    </article>
    <article class="card card--back">
      <div class="ghost-mark"><span class="ghost-mark__dot"></span><span class="ghost-mark__name">Aufwind</span></div>
      <div class="therapist-label"><span class="therapist-label__main">Behandelnder</span><span class="therapist-label__rule">|</span><span class="therapist-label__sub">Therapeut/in:</span></div>
      <div class="band"></div>
    </article>
  </section>

</main>
</body>
</html>
```